The name of my company is Tolmen Refacing LLC and I would like the sub text to say "Cabinet Refacing and Countertops". Have my name Dorian Tolmen, Owner / Sales, contact info: Cell: 360-555-0147 / Email: dorian.tolmen@quenmail.com

Simple, Clean, and Organized. With colors that will appeal to the eye.

Target Market(s)

Houses and Apartments

Industry/Entity Type

Cabinet Refacing

Contact Information for Business Card

Company name and sub text Dorian Tolmen - Owner / Sales, my cell phone number and email

Requirements
Must have
• Business name, my name / position, and my contact info
Nice to have
• Simple. Organized. Appealing to the eye

```html
<!DOCTYPE html>
<html lang="en">
<head>
<meta charset="utf-8">
<title>Tolmen Refacing LLC – Business Card</title>
<link rel="stylesheet" href="https://fonts.googleapis.com/css2?family=Montserrat:ital,wght@0,300;0,400;0,700;1,400&family=Quicksand:wght@500&display=swap">
<style>
  :root {
    --brand-blue: #4a6fbf;
    --ink: #262a2e;
    --ink-soft: #3a3d42;
    --wordmark-grey: #8d929b;
    --paper: #ffffff;
    --edge: #e4e4e4;
    --dot-tone: #f3f3f3;
  }
  * { box-sizing: border-box; margin: 0; padding: 0; }
  html, body {
    width: 1200px; height: 1200px; overflow: hidden;
    background: var(--paper);
  }
  .canvas { position: relative; width: 1200px; height: 1200px; }
  .card {
    position: absolute; left: 150px; width: 900px; height: 514px;
    background: var(--paper); border: 1px solid var(--edge); overflow: hidden;
  }
  .card--front { top: 67px; }
  .card--back { top: 622px; }

  .texture {
    position: absolute; left: 0; right: 0;
    background: linear-gradient(180deg, rgba(243,243,243,0) 0%, var(--dot-tone) 45%, var(--dot-tone) 100%);
  }
  .card--front .texture { top: 165px; bottom: 13px; }
  .card--back .texture { top: 200px; bottom: 0; }

  .brand { position: absolute; left: 0; right: 0; text-align: center; }
  .brand__mark {
    display: block; margin: 0 auto; border-radius: 50%; background: var(--brand-blue);
  }
  .brand__name {
    font-family: "Montserrat", sans-serif; font-weight: 300;
    color: var(--wordmark-grey); letter-spacing: 0.02em; white-space: nowrap;
  }
  .brand__tagline {
    font-family: "Quicksand", sans-serif; font-weight: 500; color: var(--ink);
    white-space: nowrap;
  }

  .card--front .brand { top: 26px; }
  .card--front .brand__mark { width: 44px; height: 44px; }
  .card--front .brand__name { font-size: 26px; margin-top: 18px; line-height: 1; }
  .card--front .brand__tagline { font-size: 13px; margin-top: 9px; }

  .rule { position: absolute; top: 169px; left: 53px; width: 794px; height: 5px; }
  .rule__thick { position: absolute; left: 0; top: 0; width: 384px; height: 5px; background: var(--brand-blue); }
  .rule__thin { position: absolute; left: 384px; top: 1px; right: 0; height: 3px; background: var(--brand-blue); }

  .person { position: absolute; top: 200px; left: 0; right: 0; text-align: center; }
  .person__name {
    font-family: "Montserrat", sans-serif; font-weight: 700; font-size: 35px;
    color: var(--ink); letter-spacing: 0.03em; line-height: 1;
  }
  .person__role {
    font-family: "Montserrat", sans-serif; font-style: italic; font-weight: 400;
    font-size: 17px; color: var(--ink-soft); letter-spacing: 0.05em; margin-top: 7px;
  }

  .contact { position: absolute; left: 260px; width: 420px; height: 48px; }
  .contact--phone { top: 311px; }
  .contact--email { top: 393px; }
  .contact__icon {
    position: absolute; left: 0; top: 0; width: 47px; height: 47px;
    background: var(--brand-blue); display: flex; align-items: center; justify-content: center;
  }
  .contact__line { position: absolute; left: 47px; right: 0; bottom: 0; height: 1px; background: var(--brand-blue); }
  .contact__text {
    position: absolute; left: 82px; top: 12px;
    font-family: "Montserrat", sans-serif; font-weight: 400; font-size: 17px;
    color: var(--ink); letter-spacing: 0.08em; white-space: nowrap;
  }
  .base-band { position: absolute; left: 0; right: 0; bottom: 0; height: 13px; background: var(--brand-blue); }

  .card--back .brand { top: 150px; }
  .card--back .brand__mark { width: 76px; height: 76px; }
  .card--back .brand__name { font-size: 39px; margin-top: 34px; line-height: 1; }
  .card--back .brand__tagline { font-size: 21px; margin-top: 14px; }
</style>
</head>
<body>
<main class="canvas">

  <section class="card card--front" aria-label="Business card front">
    <div class="texture" role="img" aria-label="Subtle light grey dot pattern background"></div>

    <header class="brand">
      <span class="brand__mark" aria-hidden="true"></span>
      <p class="brand__name">TOLMEN REFACING, LLC</p>
      <p class="brand__tagline">Cabinet Refacing and Countertops</p>
    </header>

    <div class="rule" aria-hidden="true">
      <span class="rule__thick"></span>
      <span class="rule__thin"></span>
    </div>

    <div class="person">
      <h1 class="person__name">DORIAN TOLMEN</h1>
      <p class="person__role">OWNER/SALES</p>
    </div>

    <div class="contact contact--phone">
      <span class="contact__icon">
        <svg width="24" height="24" viewBox="0 0 24 24" fill="none" stroke="#f1e6c8" stroke-width="1.4" stroke-linejoin="round" aria-hidden="true">
          <path d="M6.6 3.5l2.6 0 1.3 4-1.9 1.4a11 11 0 0 0 6.5 6.5l1.4-1.9 4 1.3v2.6a1.6 1.6 0 0 1-1.7 1.6A15.5 15.5 0 0 1 4.9 5.2 1.6 1.6 0 0 1 6.6 3.5z"/>
        </svg>
      </span>
      <span class="contact__line"></span>
      <span class="contact__text">360-555-0147</span>
    </div>

    <div class="contact contact--email">
      <span class="contact__icon">
        <svg width="22" height="22" viewBox="0 0 24 24" fill="none" stroke="#f1e6c8" stroke-width="1.4" aria-hidden="true">
          <circle cx="12" cy="12" r="9"/>
          <ellipse cx="12" cy="12" rx="4" ry="9"/>
          <path d="M3 12h18M4.5 7.5h15M4.5 16.5h15"/>
        </svg>
      </span>
      <span class="contact__line"></span>
      <span class="contact__text">dorian.tolmen@quenmail.com</span>
    </div>

    <div class="base-band" aria-hidden="true"></div>
  </section>

  <section class="card card--back" aria-label="Business card back">
    <div class="texture" role="img" aria-label="Subtle light grey dot pattern background"></div>
    <header class="brand">
      <span class="brand__mark" aria-hidden="true"></span>
      <p class="brand__name">TOLMEN REFACING, LLC</p>
      <p class="brand__tagline">Cabinet Refacing and Countertops</p>
    </header>
  </section>

</main>
</body>
</html>
```